Young Accounting firm needing a captivating business card

We need a business card design that forces the person to look at the card because its either gold foil, plastic, or lettering pop up etc. We already have a logo with a specific gold color and we need to make it pop. We are an accounting firm. I need the words" accounting, payroll, licenses, audits, taxes" somewhere on the business card so as to describe what we do- preferably on the side where the logo is at.

Industry/Entity Type

Accounting

Contact Information for Business Card

Address 48276 9th Ave S Ste 305, Cedar Bluff, OR 98117
Business Phone (360)418-2096
Fax (360)418-2157
Office Cell Phone (360)586-7319

Font styles to use
Serif

Colors
85abd2

Requirements
Must have
• It should state
• "Accounting" "Taxes" "Audits" "Licenses" "Payroll"
Nice to have
• Matte with gold foil, different textures, With Either a textured ivory background or gray blue slate background
Should not have
• colorful colors

```html
<!DOCTYPE html>
<html lang="en">
<head>
<meta charset="utf-8">
<title>Kestrel Ledger — Business Card</title>
<link rel="stylesheet" href="https://fonts.googleapis.com/css2?family=Cinzel:wght@600;700&family=Merriweather:wght@300;400&display=swap">
<style>
  :root {
    --gold: #b8962e;
    --ink: #3d3b38;
    --paper: #ffffff;
    --ivory: #f4eee0;
    --backdrop: #dcd8cf;
  }
  * { margin: 0; padding: 0; box-sizing: border-box; }
  html, body { width: 1200px; height: 1200px; overflow: hidden; }
  body { background: var(--backdrop); position: relative; }

  .card {
    position: absolute;
    left: 265px;
    width: 670px;
    height: 390px;
    background: var(--paper);
    overflow: hidden;
    box-shadow: 0 2px 6px rgba(0,0,0,.18);
  }
  .card--front { top: 150px; }
  .card--back { top: 590px; }

  .chevron { position: absolute; left: 0; top: 0; }

  .brand-name {
    position: absolute;
    font-family: "Cinzel", serif;
    font-weight: 700;
    color: var(--gold);
    white-space: nowrap;
    font-size: 28px;
    line-height: 1;
  }
  .card--front .brand-name { left: 40px; top: 132px; }
  .card--back .brand-name { left: 34px; top: 110px; }

  .contact-list {
    position: absolute;
    right: 33px;
    top: 138px;
    list-style: none;
    font-family: "Merriweather", serif;
    font-weight: 300;
    font-size: 18px;
    color: var(--ink);
    line-height: 26px;
  }
  .contact-list li { display: flex; align-items: center; justify-content: flex-end; gap: 8px; }
  .contact-list svg { width: 18px; height: 18px; flex: none; }

  .firm-heading {
    position: absolute;
    left: 38px;
    top: 242px;
    font-family: "Cinzel", serif;
    font-weight: 700;
    font-size: 22px;
    line-height: 1;
    color: var(--gold);
  }
  .rule {
    position: absolute;
    left: 281px;
    top: 257px;
    width: 232px;
    height: 1px;
    background: var(--gold);
  }

  .address {
    position: absolute;
    right: 33px;
    top: 298px;
    text-align: right;
    font-family: "Merriweather", serif;
    font-weight: 300;
    font-size: 18px;
    line-height: 26px;
    color: var(--ink);
    font-style: normal;
  }

  .pattern-field {
    position: absolute;
    inset: 0 0 44px 0;
    background: linear-gradient(180deg, var(--ivory), #f8f4ea);
  }
  .services {
    position: absolute;
    right: 33px;
    top: 290px;
    text-align: right;
    font-family: "Cinzel", serif;
    font-weight: 700;
    font-size: 22px;
    line-height: 26px;
    color: var(--ink);
    white-space: nowrap;
  }
  .band {
    position: absolute;
    left: 0; right: 0; bottom: 0;
    height: 44px;
    background: var(--gold);
  }
</style>
</head>
<body>

<section class="card card--front" aria-label="Card front">
  <svg class="chevron" width="670" height="390" viewBox="0 0 670 390" aria-hidden="true">
    <polygon fill="var(--gold)" points="314,24 352,24 390,90 325,208 186,208 170,176 298,176 344,90"/>
  </svg>
  <div class="brand-name">Kestrel Ledger</div>

  <ul class="contact-list">
    <li>
      <svg viewBox="0 0 18 18" aria-hidden="true"><circle cx="9" cy="9" r="8" fill="none" stroke="var(--gold)" stroke-width="1.2"/><rect x="6.3" y="4" width="5.4" height="10" rx="1" fill="none" stroke="var(--gold)" stroke-width="1.1"/></svg>
      (360)586-7319
    </li>
    <li>
      <svg viewBox="0 0 18 18" aria-hidden="true"><circle cx="9" cy="9" r="8" fill="none" stroke="var(--gold)" stroke-width="1.2"/><path d="M6 5 q-1 1 0 3 q2 4 5 5 q1.5 .5 2.2 -.6 l-1.6 -1.4 -1 .8 q-2 -1 -3 -3 l.8 -1 -1.4 -1.6z" fill="var(--gold)"/></svg>
      (360)418-2096
    </li>
    <li>
      <svg viewBox="0 0 18 18" aria-hidden="true"><circle cx="9" cy="9" r="8" fill="none" stroke="var(--gold)" stroke-width="1.2"/><rect x="5" y="7.5" width="8" height="4.5" fill="none" stroke="var(--gold)" stroke-width="1.1"/><rect x="6.5" y="4.5" width="5" height="3" fill="none" stroke="var(--gold)" stroke-width="1"/><rect x="6.5" y="11" width="5" height="2.5" fill="var(--gold)"/></svg>
      (360)418-2157
    </li>
  </ul>

  <h2 class="firm-heading">KESTREL LEDGER</h2>
  <div class="rule"></div>

  <address class="address">48276 9th Ave S Ste 305,<br>Cedar Bluff, OR-98117</address>
</section>

<section class="card card--back" aria-label="Card back">
  <div class="pattern-field" role="img" aria-label="Faint ivory repeating brand pattern background"></div>
  <div class="brand-name">Kestrel Ledger</div>
  <p class="services">ACCOUNTING, PAYROLL,<br>LICENSES, AUDITS, TAXES</p>
  <div class="band"></div>
</section>

</body>
</html>
```